Flyer-Design für bildenden Künstler
Die einzige Designerin, die es wirklich verstanden hat, mein ausführliches briefing in einem wunderschönen, eleganten und absolut einzigartigen Design umzusetzen. Die Zusammenarbeit war klasse, sie ist auf jede meiner Wünsche eingegangen und hat sie mit großer Geduld und Professionalität umgesetzt. Das hätte nicht besser laufen können. Bin begeistert, von ihrem künstlerischen Anspruch, dem feinen Sinn für Ästhetik und ihrer großen Kreativität.
Zielgruppe
Ich bin bildender Künstler, benötige einen außergewöhnlichen, sehr ästhetischen, einzigartigen, als Eyecatcher fungierenden, meine Kunst und Identität repräsentierenden Flyer zum Auslegen, um neue KundInnen zu gewinnen.
Aufgabenstellung
Er soll wenig Text beinhalten (ein Zitat, Anschrift und Kontaktmöglichkeiten, ein kleines statement zu meiner Kunstphilosophie), und Bilder meiner Kunst zeigen. Raum ist mir wichtig, genug Leerräume, damit ein in Szene gesetztes Zitat oder Foto meiner Kunstwerke gut wirken kann. Es soll Lust darauf machen, Anreiz bieten und Interesse wecken, auf meine homepage zu gehen. Die Einzigartigkeit meiner Kunst soll deutlich werden.
Die hochgelandenen Fotos zeigen meine Kunstwerke. Sie können als Hintergrundbild fungieren und dementsprechend auch die ganze Seite ausfüllen, sie können zugeschnitten werden und/oder mit Text überlagert sein. Manche Fotos (zum Beispiel die Kunstwerke mit Rahmen) eignen sich dagegen, sie auf einer ganzen Seite zu zeigen, ohne einen Text dazu. So eine Seite würde ich jedenfalls gerne dabei haben, wo ein Kunstwerk für sich alleine auf einer ganzen Seite dargestellt wird. 1O4A2598 oder 1O4A6076a bieten sich dafür an (diese und alle anderen Fotos sind zum Teil komprimiert und zugeschnitten; falls gewünscht bzw. die Qualität nicht gut ist, kann ich das Originalfoto senden, das unkomprimiert und nicht zugeschnitten ist. Auch kann die Helligkeit oder die Farbqualität verbessert werden, falls notwendig). Nicht alle Kunstbilder müssen verwendet werden.
Ich bin offen für jedes Flyerformat, tendiere zu einem ein 2 oder 3-seitigen Falzflyer hochkant oder im Querformat. Bin aber offen für Ideen und Vorschläge.
Die Texte unter der Datei 'Texte, Adresse, Zitate' enthalten einen kleinen Text, der verwendet werden soll. Unter 'Text für die Titelseite' ist ein Vorschlag für die Titelseite zu finden. Die Adresse muss vollständig erscheinen, und unter 'Zitate' sind mehrere meiner Zitate - auch davon soll eines verwendet werden.
BITTE AUSSCHLIEßLICH DIE FOTOS UND TEXTE VERWENDEN, DIE ICH HOCHGELADEN HABE, UND NICHTS VON MEINEN HOMEPAGES NEHMEN. DANKE!

```html
<!DOCTYPE html>
<html lang="de">
<head>
<meta charset="utf-8">
<title>Jens Dornhaus Art – Falzflyer</title>
<link href="https://fonts.googleapis.com/css2?family=Montserrat:wght@400;500;700;800;900&display=swap" rel="stylesheet">
<style>
  :root {
    --stage: #dde3e7;
    --paper: #f5f5f5;
    --paper-shade: #e6e6e6;
    --slate: #6f8fa4;
    --ink-teal: #2f6579;
    --ink-blue: #4f7790;
    --outline: #9a9a9a;
    --tan: #c9b392;
    --logo-ink: #2b2b2b;
    --art-light: #4aa0bd;
    --art-dark: #1f6882;
    --frame: #8d8d8d;
  }
  * { box-sizing: border-box; margin: 0; padding: 0; }
  html, body {
    width: 1200px; height: 900px; overflow: hidden;
    background: var(--stage);
    font-family: "Montserrat", sans-serif;
  }
  .canvas {
    width: 1200px; height: 900px;
    display: flex; align-items: center; justify-content: center; gap: 40px;
  }
  .spread { display: flex; box-shadow: 0 10px 30px rgba(40,60,75,.18); }
  .panel {
    position: relative; width: 190px; height: 405px;
    background: var(--paper); overflow: hidden;
  }

  /* quote panel */
  .panel--quote { background: var(--slate); color: #fff; text-align: center; }
  .quote-mark {
    position: absolute; top: 118px; left: 0; right: 0;
    font-size: 44px; font-weight: 900; line-height: 1;
  }
  .quote-text {
    position: absolute; top: 170px; left: 12px; right: 12px;
    font-size: 10.5px; font-weight: 700; line-height: 1.75;
  }

  /* contact panel */
  .rule {
    position: absolute; height: 2px; background: var(--ink-blue);
  }
  .panel--contact .rule { top: 272px; left: 0; right: 0; }
  .contact {
    position: absolute; top: 290px; left: 0; right: 0;
    text-align: center; color: var(--ink-blue);
    font-size: 8.2px; line-height: 1.3;
  }
  .contact strong { font-weight: 700; }
  .contact p + p { margin-top: 10px; }
  .contact .web { font-weight: 700; }

  /* cover */
  .panel--cover { background: var(--paper-shade); }
  .cover-title {
    position: absolute; top: 100px; left: 15px;
    font-weight: 900; font-size: 26px; line-height: 1.12;
    color: var(--ink-teal); letter-spacing: .3px;
  }
  .cover-subtitle {
    display: block; margin-top: 6px;
    font-weight: 500; font-size: 25px; line-height: 1.05;
    color: transparent; -webkit-text-stroke: 0.8px var(--outline);
    letter-spacing: .5px;
  }
  .panel--cover .rule { top: 272px; left: 0; width: 108px; }

  .brand {
    position: absolute; right: 10px; bottom: 22px;
    display: flex; align-items: center; gap: 4px;
    font-weight: 500; font-size: 12px; color: var(--logo-ink);
  }
  .brand-square { width: 7px; height: 7px; background: var(--tan); }

  /* inside */
  .panel--art { display: flex; align-items: center; justify-content: center; }
  .panel--art.is-shaded { background: var(--paper-shade); }
  .artwork-frame {
    width: 128px; height: 345px; padding: 3px;
    background: #b9b9b9; border: 1px solid var(--frame);
  }
  .artwork {
    width: 100%; height: 100%;
    background: radial-gradient(ellipse at 55% 40%, var(--art-light), var(--art-dark));
  }

  .panel--philosophy { background: #ececec; }
  .philosophy-title {
    position: absolute; top: 55px; left: 32px;
    font-weight: 800; font-size: 17px; line-height: 1.25; color: var(--ink-blue);
  }
  .philosophy-dash {
    position: absolute; top: 112px; left: 32px; width: 22px; height: 2px;
    background: var(--ink-blue);
  }
  .philosophy-text {
    position: absolute; top: 140px; left: 32px; right: 12px;
    font-size: 8.8px; line-height: 1.48; color: var(--ink-blue);
  }
</style>
</head>
<body>
<main class="canvas">

  <section class="spread spread--outside" aria-label="Außenseite">
    <div class="panel panel--quote">
      <div class="quote-mark">&ldquo;</div>
      <p class="quote-text">Kunst unterstreicht Deinen guten Geschmack. Es zeugt davon, dass Du Weitblick besitzt. Und offen für neue Erfahrungen bist.</p>
    </div>

    <div class="panel panel--contact">
      <div class="rule"></div>
      <address class="contact" style="font-style:normal">
        <p><strong>Jens Dornhaus</strong><br>Lindenhofweg 12<br>79104 Freiburg</p>
        <p>(+49) 0761 5550 1234<br>dornhaus-art@example.de</p>
        <p class="web">www.dornhaus-art.example</p>
      </address>
    </div>

    <div class="panel panel--cover">
      <h1 class="cover-title">JENS<br>DORN&shy;HAUS<br>ART
        <span class="cover-subtitle">TRANSFOR<br>MATIONEN</span>
      </h1>
      <div class="rule"></div>
      <div class="brand"><span class="brand-square"></span>Dornhaus Art</div>
    </div>
  </section>

  <section class="spread spread--inside" aria-label="Innenseite">
    <div class="panel panel--art is-shaded">
      <div class="artwork-frame">
        <div class="artwork" role="img" aria-label="Gerahmtes Kunstwerk aus türkisblau gefärbtem Moos"></div>
      </div>
    </div>

    <div class="panel panel--philosophy">
      <h2 class="philosophy-title">The<br>Philosophy</h2>
      <div class="philosophy-dash"></div>
      <p class="philosophy-text">Seit jeher fasziniert mich die Transformation eines Zustandes in einen anderen. Das ganze Leben ist eine fortwährende Veränderung, nichts bleibt, wie es ist. Ich setze mich damit auseinander und gebe Material und Vergangenem eine neue Sinnhaftigkeit.</p>
      <div class="brand"><span class="brand-square"></span>Dornhaus Art</div>
    </div>

    <div class="panel panel--art">
      <div class="artwork-frame">
        <div class="artwork" role="img" aria-label="Gerahmtes Kunstwerk aus türkisblau gefärbtem Moos, Detailansicht"></div>
      </div>
    </div>
  </section>

</main>
</body>
</html>
```